design a Print Ready DL size Daily Planner

design a Modern and fresh Branded daily planner notepad for a home builder to give out during promotions and trade shows for general use

Print Ready DL notepad 1 page to design with a to do list
Layout - set out in 1 column

Date: 1 line
Due Today: 2- 3 lines
Appointments: 2-3 lines
Top Priorities: 3 lines
Shopping: 5-10 lines

Bottom company logo website and phone number

Attached are some examples of inspiration but wrong page size and not in single column

```html
<!DOCTYPE html>
<html lang="en">
<head>
<meta charset="utf-8">
<title>Today's Plan – Daily Planner Notepad</title>
<link rel="stylesheet" href="https://fonts.googleapis.com/css2?family=PT+Sans:wght@400;700&family=PT+Sans+Narrow:wght@700&display=swap">
<style>
  :root {
    --page-bg: #f2f2f2;
    --sheet: #ffffff;
    --band: #c9b8a4;
    --band-edge: #8f8478;
    --ink: #1c1c1c;
    --rule: #7a7a7a;
  }
  html, body {
    margin: 0;
    width: 1200px;
    height: 1200px;
    overflow: hidden;
    background: var(--page-bg);
  }
  .canvas {
    position: relative;
    width: 1200px;
    height: 1200px;
  }
  .notepad {
    position: absolute;
    left: 425px;
    top: 176px;
    width: 349px;
    height: 717px;
    background: var(--sheet);
  }
  .notepad svg { display: block; }
  .band { fill: var(--band); }
  .band-edge { fill: var(--band-edge); }
  .rule { stroke: var(--rule); stroke-width: 1; }
  .checkbox { fill: none; stroke: var(--ink); stroke-width: 1; }
  .title {
    font-family: "PT Sans Narrow", "Arial Narrow", sans-serif;
    font-weight: 700;
    font-size: 34px;
    fill: var(--ink);
    letter-spacing: 0.5px;
  }
  .label {
    font-family: "PT Sans", Arial, sans-serif;
    font-size: 14.5px;
    fill: var(--ink);
  }
  .weekdays { letter-spacing: 3.2px; }
  .brand-name {
    font-family: "PT Sans", Arial, sans-serif;
    font-size: 31px;
    fill: var(--ink);
  }
  .contact {
    font-family: "PT Sans", Arial, sans-serif;
    font-size: 8.5px;
    fill: var(--ink);
  }
</style>
</head>
<body>
<main class="canvas">
  <section class="notepad" aria-label="Today's Plan daily planner sheet">
    <svg width="349" height="717" viewBox="0 0 349 717" xmlns="http://www.w3.org/2000/svg">
      <!-- Header -->
      <rect class="band" x="0" y="0" width="349" height="85"/>
      <rect class="band-edge" x="0" y="85" width="349" height="3"/>
      <text class="title" x="174.5" y="62" text-anchor="middle">TODAY’S PLAN</text>

      <!-- Date row -->
      <text class="label" x="31" y="112">Date:</text>
      <line class="rule" x1="76" y1="111.5" x2="196" y2="111.5"/>
      <text class="label weekdays" x="208" y="112">MTWTFSS</text>

      <!-- Due Today -->
      <rect class="band" x="0" y="125" width="349" height="23"/>
      <text class="label" x="31" y="141">Due Today:</text>
      <line class="rule" x1="32" y1="164.5" x2="317" y2="164.5"/>
      <line class="rule" x1="32" y1="186.5" x2="317" y2="186.5"/>
      <line class="rule" x1="32" y1="208.5" x2="317" y2="208.5"/>

      <!-- Appointments -->
      <rect class="band" x="0" y="224" width="349" height="23"/>
      <text class="label" x="31" y="240">Appointments:</text>
      <line class="rule" x1="32" y1="263.5" x2="317" y2="263.5"/>
      <line class="rule" x1="32" y1="285.5" x2="317" y2="285.5"/>
      <line class="rule" x1="32" y1="307.5" x2="317" y2="307.5"/>

      <!-- Top Priorities -->
      <rect class="band" x="0" y="323" width="349" height="23"/>
      <text class="label" x="31" y="339">Top Priorities:</text>
      <line class="rule" x1="32" y1="361.5" x2="317" y2="361.5"/>
      <line class="rule" x1="32" y1="383.5" x2="317" y2="383.5"/>
      <line class="rule" x1="32" y1="405.5" x2="317" y2="405.5"/>

      <!-- Shopping -->
      <rect class="band" x="0" y="421" width="349" height="23"/>
      <text class="label" x="31" y="437">Shopping:</text>
      <g class="shopping-list">
        <rect class="checkbox" x="32.5" y="447.5" width="12" height="12"/><line class="rule" x1="53" y1="460.5" x2="317" y2="460.5"/>
        <rect class="checkbox" x="32.5" y="469.5" width="12" height="12"/><line class="rule" x1="53" y1="482.5" x2="317" y2="482.5"/>
        <rect class="checkbox" x="32.5" y="491.5" width="12" height="12"/><line class="rule" x1="53" y1="504.5" x2="317" y2="504.5"/>
        <rect class="checkbox" x="32.5" y="513.5" width="12" height="12"/><line class="rule" x1="53" y1="526.5" x2="317" y2="526.5"/>
        <rect class="checkbox" x="32.5" y="535.5" width="12" height="12"/><line class="rule" x1="53" y1="548.5" x2="317" y2="548.5"/>
        <rect class="checkbox" x="32.5" y="557.5" width="12" height="12"/><line class="rule" x1="53" y1="570.5" x2="317" y2="570.5"/>
        <rect class="checkbox" x="32.5" y="579.5" width="12" height="12"/><line class="rule" x1="53" y1="592.5" x2="317" y2="592.5"/>
        <rect class="checkbox" x="32.5" y="601.5" width="12" height="12"/><line class="rule" x1="53" y1="614.5" x2="317" y2="614.5"/>
        <rect class="checkbox" x="32.5" y="623.5" width="12" height="12"/><line class="rule" x1="53" y1="636.5" x2="317" y2="636.5"/>
        <rect class="checkbox" x="32.5" y="645.5" width="12" height="12"/><line class="rule" x1="53" y1="658.5" x2="317" y2="658.5"/>
      </g>

      <!-- Footer -->
      <text class="brand-name" x="55" y="697">LOGO</text>
      <text class="contact" x="141" y="690">www.website.com</text>
      <text class="contact" x="216" y="690">(000) phone number</text>
    </svg>
  </section>
</main>
</body>
</html>
```